Holiday Rental Company Flyer Design (DL not A5)

Note from PixelFolk Administration: The category sizing selected is A5, however the project requires DL sized artwork. Please refer to the DL template link below while the 'Special Requirements' are updated accordingly.

Project Brief:
We need a double sided DL flyer designed for an up market Holiday Rental Company that portrays a personalised approach to property management. These are to be used for letter box drops to homes we're specifically targeting so the design should be modern, complimentary colour palette, uncluttered & visually appealing.

Please Download the DL Template from Quillmark here: http://www.quillmark.com.au/qm/ns/propath/UploadResources.aspx?selectedTab=0?pfid=BFB&pf_id=BFB&xnav=easypath-upload-image#Templates

Target Market(s)

Wealthy Home Owners

Industry/Entity Type

It Company

Font styles to use
Other font styles liked:
• Avant Garde Extra Light & Demi

Colors
33b8a4

Requirements
Must have
• DL Flyer sizes (210mm width x 99mm width, plus 3mm bleed)
• Front: Logo, Main Image & Grab
• Back: Contact Details & Brief Description of our business
• Images: Ideally the main image should be the house with the pool but alternatively a lifestyle images could also be used.
Nice to have
• A creative designer!
Should not have
• Clutter & busy designs

```html
<!DOCTYPE html>
<html lang="en">
<head>
<meta charset="utf-8">
<title>Harbourline Stays – DL Flyer</title>
<link href="https://fonts.googleapis.com/css2?family=Poppins:wght@200;300;600&display=swap" rel="stylesheet">
<style>
  :root {
    --mint: #4cf08c;
    --mint-text: #4de8a0;
    --white: #ffffff;
    --night: #0c0f6e;
    --dusk: #3a2fd0;
    --pool: #3fa8ff;
    --sea: #3fe0c0;
    --stone: #c8cfc8;
    --tile: #8a7c70;
  }
  * { margin: 0; padding: 0; box-sizing: border-box; }
  html, body { width: 1200px; height: 900px; overflow: hidden; background: var(--white); }
  body { position: relative; font-family: "Poppins", sans-serif; color: var(--mint-text); }

  .flyer { position: absolute; background: var(--white); overflow: hidden; }
  .flyer--front { left: 128px; top: 57px; width: 366px; height: 732px; }
  .flyer--back { left: 658px; top: 55px; width: 366px; height: 734px; }

  /* Front */
  .hero-photo {
    position: absolute; left: 0; top: 0; width: 366px; height: 484px;
    background: linear-gradient(180deg, var(--night) 0%, var(--dusk) 40%, #6a5ad0 62%, var(--pool) 78%, #9fe6ff 100%);
  }
  .front-band { position: absolute; left: 0; top: 484px; width: 366px; height: 29px; background: var(--mint); }
  .brand-name {
    position: absolute; left: 0; width: 366px; text-align: center;
    font-weight: 200; color: var(--mint-text); text-transform: uppercase;
  }
  .brand-name--front { top: 518px; font-size: 38px; line-height: 48px; letter-spacing: 3px; }
  .brand-mark {
    position: absolute; border: 1px solid var(--mint-text); border-radius: 50%;
  }
  .brand-mark--front { left: 160px; top: 630px; width: 46px; height: 46px; }
  .tagline-band {
    position: absolute; left: 0; top: 695px; width: 366px; height: 37px; background: var(--mint);
    color: var(--white); font-weight: 600; font-size: 13.5px; line-height: 37px; text-align: center;
  }

  /* Back */
  .gallery { position: absolute; left: 8px; top: 0; width: 350px; height: 110px; }
  .gallery-photo { position: absolute; top: 0; width: 113px; height: 110px; border-radius: 0 0 12px 12px; }
  .gallery-photo--seals { left: 0; background: linear-gradient(160deg, #7ff5e0, var(--sea) 60%, #2cc9a8); }
  .gallery-photo--basin { left: 118px; background: linear-gradient(180deg, #9aa59c, var(--stone) 55%, #f1f3f0); }
  .gallery-photo--flowers { left: 236px; width: 114px; background: linear-gradient(180deg, #b89f88, var(--tile) 55%, #2c3a80); }

  .copy { position: absolute; left: 30px; width: 306px; text-align: center; }
  .copy-heading { top: 158px; font-weight: 600; font-size: 13px; line-height: 16px; }
  .copy-intro { top: 192px; font-weight: 300; font-size: 12px; line-height: 17px; }
  .copy-lead { top: 293px; font-weight: 600; font-size: 12.5px; line-height: 17px; }
  .service-list { top: 361px; list-style: none; font-weight: 300; font-size: 12px; line-height: 17px; }
  .contact-prompt { top: 491px; font-weight: 600; font-size: 10.5px; line-height: 14px; }
  .contact-details { top: 542px; font-weight: 300; font-size: 10px; line-height: 17px; font-style: normal; }
  .contact-details span + span { margin-left: 12px; }
  .brand-name--back { top: 610px; font-size: 20px; line-height: 24px; letter-spacing: 1.5px; }
  .brand-mark--back { left: 172px; top: 670px; width: 22px; height: 22px; }
</style>
</head>
<body>

  <section class="flyer flyer--front" aria-label="Flyer front">
    <div class="hero-photo" role="img" aria-label="Photo of a modern house at dusk with a lit swimming pool and water feature"></div>
    <div class="front-band"></div>
    <h1 class="brand-name brand-name--front">Harbourline<br>Stays</h1>
    <div class="brand-mark brand-mark--front"></div>
    <p class="tagline-band">Holiday Rental Management with a difference</p>
  </section>

  <section class="flyer flyer--back" aria-label="Flyer back">
    <div class="gallery">
      <div class="gallery-photo gallery-photo--seals" role="img" aria-label="Photo of seals swimming in turquoise water"></div>
      <div class="gallery-photo gallery-photo--basin" role="img" aria-label="Photo of a stone bathroom basin with tap and flowers"></div>
      <div class="gallery-photo gallery-photo--flowers" role="img" aria-label="Photo of bird of paradise flowers in a vase with candles"></div>
    </div>

    <h2 class="copy copy-heading">What we do differently!</h2>
    <p class="copy copy-intro">Rather than relying upon a key safe or a central pick-up destination, a Harbourline Stays staff member will greet guests upon arrival.</p>
    <p class="copy copy-lead">Our ‘Meet &amp; Greet’ service provides home owners with an increased level of Security and also allows us to:</p>
    <ul class="copy service-list">
      <li>Prepare the home for their arrival (lights, heaters, music etc.)</li>
      <li>Establish a rapport &amp; help facilitate future bookings</li>
      <li>Reiterate their responsibilities to ensure the return of their bond</li>
    </ul>
    <p class="copy contact-prompt">If you’d like to know what your property could achieve or require additional information, please contact us on:</p>
    <address class="copy contact-details">
      <div><span>t: (03)5900 4172</span><span>e: stay@harbourlinestays.com.au</span></div>
      <div>w: harbourlinestays.com.au</div>
      <div>PO Box 12, Seaview Victoria 3900</div>
    </address>
    <p class="brand-name brand-name--back">Harbourline<br>Stays</p>
    <div class="brand-mark brand-mark--back"></div>
  </section>

</body>
</html>
```